Cover für Hauptkatalog
Zielgruppe
TESSARIN GmbH ist ein führender Großhändler in der Hobby- und Bastelbranche. mit unseren weit über 8.000 Produkten beliefern wir Einzelhändler in ganz Europa. Durch unsere Größe sind wir in der Lage sehr schnell auf individuelle Kundenwünsche zu reagieren.
Aufgabenstellung
Wir werden Mitte Dezember einen neuen Kreativ-Katalog mit über 450 Seiten unseren Kunden zur Verfügung stellen. In diesem Zusammenhang soll der Umschlag (Vorder- und Rückseite) in einem neuen, frischen Design erscheinen. Das aktuelle Layout kann unter www.tessarin-hobby.example eingesehen werden. Auf der Rückseite soll unsere Adresse stehen.

```html
<!DOCTYPE html>
<html lang="de">
<head>
<meta charset="utf-8">
<title>TESSARIN Katalog – Rückseite</title>
<link rel="stylesheet" href="https://fonts.googleapis.com/css2?family=Roboto:wght@400;700&display=swap">
<style>
  :root {
    --paper: #ffffff;
    --ink: #333333;
    --band: #ecc4d6;
    --owl-blue: #3cb6de;
    --owl-pink: #f2b4cb;
    --brand-blue: #1f3f8f;
  }
  * { margin: 0; padding: 0; box-sizing: border-box; }
  html, body { width: 848px; height: 1200px; overflow: hidden; background: var(--paper); }
  body { font-family: "Roboto", Arial, sans-serif; color: var(--ink); position: relative; }

  .hero-figure {
    position: absolute; left: 147px; top: 96px; width: 561px; height: 532px;
  }
  .accent-band {
    position: absolute; left: 0; top: 641px; width: 848px; height: 12px; background: var(--band);
  }

  .info-block {
    position: absolute; right: 51px; top: 738px; text-align: right;
  }
  .site-url { font-size: 18px; font-weight: 700; line-height: 22px; }
  .site-sub { font-size: 13px; line-height: 18px; }
  .info-note { margin-top: 20px; font-size: 13.5px; line-height: 18.5px; }

  .address-columns {
    position: absolute; right: 51px; top: 884px; display: flex; gap: 66px; text-align: right;
  }
  .address-card h2 { font-size: 18px; font-weight: 700; line-height: 24px; margin-bottom: 4px; }
  .address-card p { font-size: 13.5px; line-height: 18.6px; }

  .brand-mark {
    position: absolute; left: 0; width: 848px; top: 1118px;
    display: flex; justify-content: center; align-items: center; gap: 10px;
  }
  .brand-name {
    font-size: 38px; font-weight: 700; color: var(--brand-blue); letter-spacing: 0;
  }
  .brand-square { width: 24px; height: 24px; background: var(--brand-blue); }
</style>
</head>
<body>
  <svg class="hero-figure" viewBox="0 0 561 532" role="img" aria-label="Foto einer bemalten Pappmaché-Eule in Türkis und Rosa mit bunten Glassteinen">
    <defs>
      <linearGradient id="owlTone" x1="0" y1="0" x2="0" y2="1">
        <stop offset="0" stop-color="#3cb6de"/>
        <stop offset="0.55" stop-color="#4fbde0"/>
        <stop offset="1" stop-color="#f2b4cb"/>
      </linearGradient>
    </defs>
    <path d="M150 0 L410 0 Q430 200 561 532 L0 532 Q120 220 150 0 Z" fill="url(#owlTone)"/>
  </svg>

  <div class="accent-band"></div>

  <div class="info-block">
    <p class="site-url">www.tessarin-hobby.example</p>
    <p class="site-sub">NEUHEUTEN D | F | GB</p>
    <div class="info-note">
      <p>Weitere Informationen und Bezugsquellennachweis</p>
      <p>Pour Toute information complemenaire et liste de revendeurs</p>
      <p>Further information and documentation can be obtained from</p>
    </div>
  </div>

  <div class="address-columns">
    <div class="address-card">
      <h2>TESSARIN GmbH</h2>
      <p>Lindenweg 14</p>
      <p>79100 Mühlbach</p>
      <p>T. +49 7000 41 28-0</p>
      <p>F. +49 7000 41 29</p>
      <p>info@tessarin-hobby.example</p>
    </div>
    <div class="address-card">
      <h2>TESSARIN AG</h2>
      <p>Seeweg 8</p>
      <p>CH-4000 Bergtal</p>
      <p>T. +41 00 555 20 10</p>
      <p>F. +41 00 555 20 11</p>
      <p>kontakt@tessarin-hobby.example</p>
    </div>
  </div>

  <div class="brand-mark">
    <span class="brand-name">TESSARIN</span>
    <span class="brand-square"></span>
  </div>
</body>
</html>
```